Whitepaper: 7 Keys to Achieving Success of Your RTLS Initiative

Create a graphical layout for a whitepaper that would include 7 illustrations matching each subject line. Colors aligned with Maplewire branding guide (attached)
Updates

Just to summarize, I would need graphics/illustrations for 7 bullet points - Key #1: Set Measurements for Success Key #2: Establish a Clear Roadmap Key #3: Don’t Use Pilots (small try out of software) Key #4: Plan for the Future, from the Start Key #5: Think about RTLS as an Initiative, not a Project Key #6: Nurture the Change Key #7: Show Successes, Early

I would expect about 2-3 illustrations per page. Format - US size 8.5x11. PDF file, but would like to have the ability to edit text if needed. Thank you for your interest. Colors don't need to match the branding. It is a healthcare whitepaper so it could be blue and green.

Project Deadline Extended
Reason: Some of you have asked for a time extension.

```html
<!DOCTYPE html>
<html lang="en">
<head>
<meta charset="utf-8">
<title>7 Keys to Achieving Success of Your RTLS Initiative — Keys 3 and 4</title>
<link href="https://fonts.googleapis.com/css2?family=Raleway:wght@300;400;600;700&display=swap" rel="stylesheet">
<style>
  :root {
    --backdrop: #fdf1d3;
    --paper: #ffffff;
    --ink: #3e3d4a;
    --body-ink: #4a4a55;
    --rule: #8a8a8a;
    --key-red: #c0393b;
    --key-coral: #ec5f5d;
    --band-blue: #5a6cb0;
    --on-band: #ffffff;
  }
  * { margin: 0; padding: 0; box-sizing: border-box; }
  html, body { width: 900px; height: 1200px; overflow: hidden; }
  body {
    background: var(--backdrop);
    font-family: "Raleway", Arial, sans-serif;
    font-variant-numeric: lining-nums;
    color: var(--ink);
    position: relative;
  }
  .page {
    position: absolute;
    left: 55px; top: 50px;
    width: 793px; height: 1028px;
    background: var(--paper);
    box-shadow: 4px 5px 6px rgba(0,0,0,0.28);
    overflow: hidden;
  }
  .section-rule {
    position: absolute;
    left: 0; right: 0; top: 80px;
    height: 1px;
    background: var(--rule);
  }
  .key-pill {
    position: absolute;
    width: 138px; height: 40px;
    border-radius: 20px;
    color: #fff;
    font-weight: 700;
    font-size: 21px;
    line-height: 40px;
    text-align: center;
  }
  .key-three-pill { left: 319px; top: 58px; background: var(--key-red); }
  .key-four-pill { left: 319px; top: 462px; background: var(--key-coral); z-index: 2; }

  .key-title {
    font-weight: 700;
    font-size: 16px;
    line-height: 19px;
  }
  .key-body {
    font-weight: 300;
    font-size: 15px;
    letter-spacing: 0.35px;
    line-height: 18.75px;
  }
  .key-body .line {
    display: block;
    white-space: nowrap;
    text-align: justify;
    text-align-last: justify;
  }
  .key-body .line.last { text-align-last: left; }

  .pilot-text {
    position: absolute;
    left: 328px; top: 117px;
    width: 392px;
    color: var(--body-ink);
  }
  .pilot-text .key-title { color: var(--ink); }
  .pilot-illustration {
    position: absolute;
    left: 113px; top: 155px;
    width: 162px; height: 253px;
    background: linear-gradient(160deg, #6a6973 0%, #45444f 100%);
    border-radius: 6px;
  }

  .future-band {
    position: absolute;
    left: 0; top: 443px;
    width: 793px; height: 284px;
  }
  .future-text {
    position: absolute;
    left: 73px; top: 507px;
    width: 392px;
    color: var(--on-band);
  }
  .future-text .key-body { margin-top: 1px; }
  .future-illustration {
    position: absolute;
    left: 510px; top: 500px;
    width: 180px; height: 200px;
    background: radial-gradient(circle, #8694c9 0%, #5a6cb0 75%);
    border-radius: 50%;
  }

  .pull-quote {
    position: absolute;
    left: 0; right: 0; top: 770px;
    text-align: center;
    font-weight: 700;
    font-size: 32.5px;
    line-height: 37.5px;
    color: var(--ink);
  }
  .brand-mark {
    position: absolute;
    left: 0; right: 0; top: 958px;
    text-align: center;
    font-weight: 600;
    font-size: 22px;
    color: var(--ink);
  }
</style>
</head>
<body>
  <main class="page">
    <div class="section-rule"></div>
    <div class="key-pill key-three-pill">Key #3</div>

    <div class="pilot-illustration" role="img" aria-label="Illustration of an RTLS value test tube crossed out, pouring into a flask over a candle"></div>

    <section class="pilot-text">
      <h2 class="key-title">Don’t Use Pilots to Test the RTLS Value</h2>
      <p class="key-body">
        <span class="line">It is important to understand that RTLS technology</span>
        <span class="line">has a certain threshold by which it becomes useful.</span>
        <span class="line">So often, when new technologies are presented to</span>
        <span class="line">our organizations, we tend to say: “Well, let’s do a</span>
        <span class="line">little pilot, maybe in the ED or one clinic, and let’s see</span>
        <span class="line">if this is really going to do all these things a vendor</span>
        <span class="line">claims it will.” That’s not going to work for you with re-</span>
        <span class="line">al-time location technologies because the true value</span>
        <span class="line">comes when you can “light up” the entire organiza-</span>
        <span class="line">tion. Unless you can “see” your entire system, you will</span>
        <span class="line">be missing a whole lot of benefits RTLS technology</span>
        <span class="line">can provide. Additionally, the technologies have</span>
        <span class="line">reached a point of adoption that it is easy to find out</span>
        <span class="line">how they have performed in the real-world from</span>
        <span class="line">other organizations that have deployed them and</span>
        <span class="line last">have years of experience with using them..</span>
      </p>
    </section>

    <svg class="future-band" viewBox="0 0 793 284" aria-hidden="true">
      <polygon points="0,0 66,37 793,37 793,284 0,284" fill="var(--band-blue)"/>
    </svg>
    <div class="key-pill key-four-pill">Key #4</div>

    <section class="future-text">
      <h2 class="key-title">Plan for the Future, from the Start</h2>
      <p class="key-body">
        <span class="line">The Real-Time Technologies are becoming cheaper,</span>
        <span class="line">faster, and better with each day. Therefore, you want</span>
        <span class="line">to design your RTLS solution to accommodate this</span>
        <span class="line">ongoing versatility and innovation. So don’t wed your-</span>
        <span class="line">self to a company that offers one particular sensing</span>
        <span class="line">technology or is very proprietary in nature. You want</span>
        <span class="line">someone that can play nice with all the vendors and</span>
        <span class="line last">new technologies that are evolving in this space.</span>
      </p>
    </section>

    <div class="future-illustration" role="img" aria-label="Atom diagram linking You, New Technology and Vendors around the Future"></div>

    <blockquote class="pull-quote">“Design your RTLS solution<br>to accommodate ongoing versatility<br>and innovation”</blockquote>

    <div class="brand-mark">Maplewire</div>
  </main>
</body>
</html>
```